Website redesign for Brightwater Drip Clinic

We need website redesign for Brightwater Drip Clinic - Natural Health & Wellness Center.
In addition to our IV Infusions & Intramuscular Injection, our team offers a full spectrum of natural healing modalities to optimize physical, emotional and spiritual well being.
our current website is www.brightwaterdripclinic.com
Our major competitor is https://calmorrahub.com/
See uploaded design of current logo.
Target Market(s)
Health, fitness, functional medicine, immune boosting, alternative medicine, holistic medicine, supplements
Industry/Entity Type
Health And Wellness
Logo Text
Brightwater Drip Clinic - Natural Health & Wellness Center
Number of Pages Required
5+ page
Requirements
Must have
- Contemporary Professional / Medical / Health Professional Look
Our current website is www.brightwaterdripclinic.com

```html
<!DOCTYPE html>
<html lang="en">
<head>
<meta charset="utf-8">
<title>Brightwater Drip Clinic - Natural Health &amp; Wellness Center</title>
<link rel="stylesheet" href="https://fonts.googleapis.com/css2?family=Ubuntu:wght@300;400;500&family=Tinos&family=Raleway:wght@500;600&display=swap">
<style>
:root{
  --navy:#2d3561;
  --lime:#c1e021;
  --teal:#4ba8bc;
  --heading:#1f2433;
  --health:#3b5f8c;
  --muted:#8a8f98;
  --footer:#2a2a2c;
  --white:#ffffff;
}
*{box-sizing:border-box;margin:0;padding:0}
html,body{width:1200px;height:4080px;overflow:hidden}
body{position:relative;background:var(--white);font-family:"Ubuntu",sans-serif;color:var(--heading)}
.abs{position:absolute}
/* header */
.site-header{left:0;top:0;width:1200px;height:65px;background:var(--white)}
.brand{left:50px;top:17px;display:flex;align-items:center;gap:9px}
.brand-dot{width:28px;height:28px;border-radius:50%;background:var(--navy)}
.brand-name{font-size:16px;font-weight:500;color:var(--navy)}
.main-nav{right:42px;top:24px;display:flex;gap:16px;font-size:15px;color:var(--heading)}
/* hero */
.hero{left:0;top:65px;width:1200px;height:621px;background:linear-gradient(90deg,#f4f5f7 0%,#eceef1 55%,#dfe3e8 100%)}
.hero-photo{left:700px;top:65px;width:500px;height:621px;background:linear-gradient(135deg,#e8edf1 0%,#b9cfe0 40%,#d59a55 62%,#6f8b3a 80%,#dfe5ea 100%)}
.hero-title{left:50px;top:188px;font-size:37px;line-height:52px;font-weight:400;color:var(--heading)}
.hero-text{left:50px;top:312px;width:520px;font-size:16.5px;line-height:29px;color:var(--heading)}
.btn-book{left:47px;top:436px;width:209px;height:52px;background:var(--navy);color:var(--white);border-radius:5px;font-size:19px;display:flex;align-items:center;justify-content:center}
/* section titles */
.section-title{left:0;width:1200px;text-align:center;font-size:44px;font-weight:400;color:var(--heading)}
/* packages */
.pack{color:var(--white);padding:0 0 0 32px}
.pack-navy{background:var(--navy);top:880px;height:413px;width:346px}
.pack-lime{background:var(--lime);color:var(--heading);top:839px;height:476px;width:346px}
.pack h3{font-size:26px;font-weight:400;margin-bottom:20px}
.pack ul{list-style:none;font-size:14px;line-height:18px;padding-left:21px}
.pack li{margin-bottom:14px}
.pack .link{font-size:14px;display:inline-flex;align-items:center;gap:18px;padding-bottom:4px;border-bottom:1.5px solid currentColor;margin-top:34px;margin-left:8px}
/* menu */
.menu-band{left:0;top:1525px;width:1200px;height:1108px;background:var(--navy)}
.pill{height:35px;border:2px solid var(--white);border-radius:18px;color:var(--white);font-family:"Raleway",sans-serif;font-weight:500;font-size:19px;letter-spacing:2.5px;display:flex;align-items:center;justify-content:center}
.pill.active{background:var(--lime);border-color:var(--lime);color:var(--navy);font-weight:600}
.menu-photo{left:62px;top:1746px;width:539px;height:807px;background:linear-gradient(160deg,#cfcbc3 0%,#9d978d 45%,#f1f1f1 70%,#2f6fb8 100%)}
.infusion{left:640px;top:1738px;width:500px;color:var(--white)}
.infusion h2{font-family:"Raleway",sans-serif;font-weight:500;font-size:32px;letter-spacing:3px}
.infusion .tagline{font-family:"Raleway",sans-serif;font-weight:500;color:var(--lime);font-size:21px;letter-spacing:2.5px;line-height:29px;margin-top:12px}
.infusion p,.infusion li{font-family:"Tinos",serif;font-size:16px;line-height:25px}
.infusion .lead{margin-top:16px}
.infusion ul{list-style:none;margin:18px 0 0 18px}
.infusion li{line-height:28px}
.infusion .inside{margin:12px 0 0 4px}
.ingredient{margin:10px 0 0 4px}
.ingredient dt{font-family:"Tinos",serif;color:var(--lime);font-size:16px;line-height:28px}
.ingredient dd{font-family:"Tinos",serif;font-size:16px;line-height:25px;margin-bottom:23px}
.btn-lime{left:644px;top:2528px;width:180px;height:41px;background:var(--lime);color:var(--navy);font-size:21px;border-radius:4px;display:flex;align-items:center;justify-content:center}
/* services */
.health-title{left:72px;top:2705px;font-size:40px;line-height:58px;color:var(--health);font-weight:400}
.health-text{left:74px;top:2838px;width:290px;font-family:"Tinos",serif;font-size:16px;line-height:25.5px;color:var(--heading)}
.service{width:200px;text-align:center}
.service svg{display:block;margin:0 auto 10px}
.service h4{font-size:15px;font-weight:400;color:var(--heading);margin-bottom:22px}
.service h4.u{text-decoration:underline}
.service p{font-size:10.5px;line-height:14.5px;color:var(--muted)}
/* newsletter */
.news{left:0;top:3690px;width:1200px;height:188px;background:var(--navy)}
.news-title{left:58px;top:3763px;font-size:40px;color:var(--white);font-weight:400}
.news-input{left:541px;top:3762px;width:362px;height:51px;border:2px solid var(--white);color:var(--white);font-size:14px;display:flex;align-items:center;padding-left:21px}
.news-btn{left:901px;top:3762px;width:218px;height:51px;background:var(--lime);color:var(--navy);font-size:14px;display:flex;align-items:center;justify-content:center}
/* footer */
.footer{left:0;top:3878px;width:1200px;height:202px;background:var(--footer)}
.divider{width:2px;height:135px;background:var(--white);top:3912px}
.contact{font-family:"Tinos",serif;color:var(--white);font-size:21px;line-height:33px}
</style>
</head>
<body>

<header class="abs site-header">
  <div class="abs brand"><span class="brand-dot"></span><span class="brand-name">Brightwater Drip Clinic</span></div>
  <nav class="abs main-nav"><span>HOME</span><span>SERVICES</span><span>INTAKE FORMS</span><span>PRODUCTS</span><span>OUR TEAM</span><span>BOOK ONLINE</span><span>CONTACT US</span></nav>
</header>

<section class="abs hero"></section>
<div class="abs hero-photo" role="img" aria-label="Gloved hand holding an IV bag filled with sliced fruit"></div>
<h1 class="abs hero-title">WELCOME TO BRIGHTWATER DRIP CLINIC<br>NATURAL HEALTH &amp; WELLNESS</h1>
<p class="abs hero-text">Our team offers a full spectrum of healing modalities to optimize your physical, emotional and spiritual well being. Check out our list of treatments and services below.</p>
<div class="abs btn-book">BOOK A SESSION</div>

<h2 class="abs section-title" style="top:726px">OUR PACKAGES</h2>

<article class="abs pack pack-navy" style="left:81px;padding-top:40px">
  <svg width="68" height="62" viewBox="0 0 68 62" style="margin-left:8px"><path d="M34 58 C10 40 4 28 6 17 C8 6 22 2 34 16 C46 2 60 6 62 17 C64 28 58 40 34 58Z" fill="none" stroke="#fff" stroke-width="4"/></svg>
  <h3 style="margin-top:14px">4 PACK IVS</h3>
  <ul><li>4 Pack - $500 &nbsp;includes:</li><li>Any four IV Infusions</li><li>Regular price $175 ea</li><li>Total Package Value &nbsp;&nbsp;&nbsp;&nbsp;$700 ($200 savings)</li><li>Your price &nbsp;$125 each</li></ul>
  <span class="link">Book Now <svg width="30" height="10" viewBox="0 0 30 10"><path d="M0 5H28M23 1L28 5L23 9" stroke="currentColor" stroke-width="1.8" fill="none"/></svg></span>
</article>

<article class="abs pack pack-lime" style="left:427px;padding-top:34px">
  <svg width="78" height="78" viewBox="0 0 78 78" style="margin-left:7px"><circle cx="39" cy="39" r="35" fill="none" stroke="#1f2433" stroke-width="4"/><path d="M39 20V58M20 39H58" stroke="#1f2433" stroke-width="9"/></svg>
  <h3 style="margin-top:14px">12 PACK IVS</h3>
  <ul style="padding-left:37px"><li>2 Pack - $1200 includes:</li><li>Any twelve IV Infusions</li><li>Regular price $175 ea</li><li>Total Package Value &nbsp;&nbsp;&nbsp;&nbsp;$2100 ($900 savings)</li></ul>
  <span class="link">Book Now <svg width="30" height="10" viewBox="0 0 30 10"><path d="M0 5H28M23 1L28 5L23 9" stroke="currentColor" stroke-width="1.8" fill="none"/></svg></span>
</article>

<article class="abs pack pack-navy" style="left:773px;padding-top:30px">
  <svg width="44" height="62" viewBox="0 0 44 62" style="margin-left:14px"><path d="M22 4 C28 18 40 30 40 42 A18 18 0 0 1 4 42 C4 30 16 18 22 4Z" fill="none" stroke="#fff" stroke-width="3"/></svg>
  <h3 style="margin-top:16px">6 PACK IVS</h3>
  <ul style="padding-left:31px"><li>4 Pack - $500 &nbsp;includes:</li><li>Any four IV Infusions</li><li>Regular price $175 ea</li><li>Total Package Value &nbsp;&nbsp;&nbsp;&nbsp;$700 ($200 savings)</li><li>Your price &nbsp;$125 each</li></ul>
  <span class="link">Book Now <svg width="30" height="10" viewBox="0 0 30 10"><path d="M0 5H28M23 1L28 5L23 9" stroke="currentColor" stroke-width="1.8" fill="none"/></svg></span>
</article>

<h2 class="abs section-title" style="top:1437px">IV INFUSION MENU</h2>

<section class="abs menu-band"></section>
<div class="abs pill" style="left:47px;top:1569px;width:197px">INNER BEAUTY</div>
<div class="abs pill active" style="left:284px;top:1569px;width:196px">ALLEVIATE PMS</div>
<div class="abs pill" style="left:503px;top:1569px;width:227px">MYER’S COCKTAIL</div>
<div class="abs pill" style="left:748px;top:1569px;width:159px">IMMUNITY</div>
<div class="abs pill" style="left:926px;top:1569px;width:122px">QUENCH</div>
<div class="abs pill" style="left:45px;top:1628px;width:211px">GET UP AND GO</div>
<div class="abs pill" style="left:307px;top:1628px;width:357px">RECOVERY AND PERFOMANCE</div>
<div class="abs pill" style="left:716px;top:1628px;width:243px">BOOSTES WITH IV’S</div>

<div class="abs menu-photo" role="img" aria-label="Young man in a white shirt and cap holding his head in discomfort"></div>

<div class="abs infusion">
  <h2>ALLEVIATE PMS | $150</h2>
  <p class="tagline">REDUCE BLOATING, IRRITABILITY,<br>ABDOMINAL DISCOMFORT AND MORE</p>
  <p class="lead">Compounded to help relieve symptoms of PMS, this customized drip includes premium-quality compounds which may reduce bloating, irritability, abdominal discomfort and lower back pain.</p>
  <ul><li>-Helps minimize bloating</li><li>-Reduces abdominal discomfort</li><li>-Improves irritability</li><li>-Helps decrease lower back pain</li></ul>
  <p class="inside">What’s inside:</p>
  <dl class="ingredient">
    <dt>B-Complex Vitamins</dt><dd>B-complex vitamins may help keep skin and blood cells healthy as well as convert nutrients into energy.</dd>
    <dt>Calcium Chloride</dt><dd>&nbsp;Calcium helps promote healthy bones and the normal functioning of muscles, nerves and cells in the body.</dd>
    <dt>Hydroxo B12</dt><dd>Hydroxo B12 is designed to help treat low levels of Vitamin B12, as well as promote healthy brain function, blood, cells and nerves.</dd>
    <dt>Magnesium Chloride</dt><dd>Magnesium chloride can help improve immunity, decrease risk of developing migraines, improve relaxation and more.</dd>
  </dl>
</div>
<div class="abs btn-lime">BOOK NOW</div>

<h2 class="abs health-title">TAKING CARE OF<br>YOUR HEALTH</h2>
<p class="abs health-text">Services offered from Comprehensive exams to sports and physicals, Men’s Health, Medical Cannabis Certifications, Hormonal Therapy, Testosterone and B12 supplementation, Immigration Exams, and many other services. Bilingual (Spanish and English).</p>

<div class="abs service" style="left:436px;top:2685px">
  <svg width="40" height="56" viewBox="0 0 40 56"><rect x="6" y="2" width="28" height="30" rx="6" fill="#4ba8bc"/><path d="M20 32V44" stroke="#4ba8bc" stroke-width="3"/><path d="M20 44C23 49 24 51 20 54C16 51 17 49 20 44Z" fill="#4ba8bc"/></svg>
  <h4>IV Nutrition Therapy</h4><p>Direct infusion of vitamins and minerals, like high doses of vitamin C or magnesium.</p>
</div>
<div class="abs service" style="left:700px;top:2685px">
  <svg width="46" height="60" viewBox="0 0 46 60"><path d="M16 4H30M18 4V22L4 54H42L28 22V4" fill="none" stroke="#4ba8bc" stroke-width="4"/><path d="M11 40H35L41 54H5Z" fill="#4ba8bc"/></svg>
  <h4>Lab Services</h4><p>We provide our clients with access to over 6000 individual tests, test panels.</p>
</div>
<div class="abs service" style="left:964px;top:2680px">
  <svg width="54" height="70" viewBox="0 0 54 70"><rect x="3" y="8" width="48" height="60" rx="6" fill="none" stroke="#4ba8bc" stroke-width="3"/><rect x="16" y="2" width="22" height="12" rx="3" fill="#4ba8bc"/><path d="M15 42H39M15 50H39M15 58H39M27 22V34M21 28H33" stroke="#4ba8bc" stroke-width="2.5"/></svg>
  <h4>Health Report</h4><p>Reports convert standard lab results to uncover dysfunction areas from a functional health perspective.</p>
</div>

<div class="abs service" style="left:436px;top:2955px">
  <svg width="56" height="60" viewBox="0 0 56 60"><circle cx="28" cy="30" r="26" fill="none" stroke="#4ba8bc" stroke-width="1.5"/><path d="M20 46V26M26 44V20M32 44V22M38 42V28" stroke="#4ba8bc" stroke-width="1.5"/></svg>
  <h4>Veris Bioscan</h4><p>VERIS helps you design a personalized health and nutrition program specific to your body’s needs.</p>
</div>
<div class="abs service" style="left:700px;top:2950px">
  <svg width="72" height="72" viewBox="0 0 72 72"><circle cx="36" cy="36" r="12" fill="none" stroke="#4ba8bc" stroke-width="5"/><g stroke="#4ba8bc" stroke-width="5"><path d="M36 2V20M36 52V70M2 36H20M52 36H70M12 12L25 25M47 47L60 60M60 12L47 25M25 47L12 60"/></g></svg>
  <h4>Lumen Laser Therapy</h4><p>Class IV Laser manages pain and inflammation while accelerating tissue regeneration</p>
</div>
<div class="abs service" style="left:964px;top:2955px">
  <svg width="56" height="60" viewBox="0 0 56 60"><path d="M28 4L52 18L48 48L28 56L8 48L4 18Z M28 4L20 30L28 56L36 30Z M4 18L20 30L48 48 M52 18L36 30L8 48" fill="none" stroke="#4ba8bc" stroke-width="1.5"/></svg>
  <h4>Osciva 200</h4><p>Deep Oscillation Therapy for muscle relaxation, pain relief, and increasing circulation.</p>
</div>

<div class="abs service" style="left:436px;top:3225px">
  <svg width="36" height="66" viewBox="0 0 36 66"><path d="M4 4H32V22A14 14 0 0 1 4 22Z" fill="#4ba8bc"/><path d="M18 36V60M8 62H28" stroke="#4ba8bc" stroke-width="3"/></svg>
  <h4 class="u">Chinese Cupping </h4><p>Helps with pain, inflammation, blood flow, relaxation and well-being, and as a type of deep-tissue massage.</p>
</div>
<div class="abs service" style="left:700px;top:3225px">
  <svg width="76" height="66" viewBox="0 0 76 66"><path d="M14 30V10A7 7 0 0 1 28 10" fill="none" stroke="#4ba8bc" stroke-width="2.5"/><rect x="4" y="30" width="68" height="8" rx="2" fill="none" stroke="#4ba8bc" stroke-width="2.5"/><path d="M8 38V48A10 10 0 0 0 18 58H58A10 10 0 0 0 68 48V38" fill="none" stroke="#4ba8bc" stroke-width="2.5"/><path d="M18 58L14 64M58 58L62 64" stroke="#4ba8bc" stroke-width="2.5"/></svg>
  <h4 class="u">Detox Footbath</h4><p>Improve your health through cellular detoxification with the Aqua Purge Detox Footbath from Clearwell.</p>
</div>
<div class="abs service" style="left:964px;top:3235px">
  <svg width="60" height="50" viewBox="0 0 60 50"><path d="M8 14L20 10L24 24L14 30Z" fill="#a9cfe3"/><path d="M36 18L50 12L56 26L46 38L34 32Z" fill="#4ba8bc"/></svg>
  <h4>Crystal Bath</h4><p>Seven clear and highly polished Lindqvist cut quartz crystals cleanse, balance, and align your energies.</p>
</div>

<div class="abs service" style="left:436px;top:3438px">
  <svg width="70" height="46" viewBox="0 0 70 46"><path d="M8 12L16 4L66 34L58 42Z" fill="#4ba8bc"/><path d="M8 12L16 4L24 9L16 17Z" fill="#a9cfe3"/></svg>
  <h4 class="u">Smoking Cessation Program</h4><p>This program provides more than the standard treatment for nicotine dependence, it offers a complete, integrative medical approach to treating your tobacco dependence addressing all aspects - mind, body &amp; spirit.</p>
</div>

<section class="abs news"></section>
<h2 class="abs news-title">NEVER MISS AN UPDATE</h2>
<div class="abs news-input">ENTER YOUR EMAIL HERE</div>
<div class="abs news-btn">JOIN OUR MAILING LIST</div>

<footer class="abs footer"></footer>
<div class="abs divider" style="left:339px"></div>
<div class="abs divider" style="left:754px"></div>
<div class="abs contact" style="left:92px;top:3930px">CALL US<br>555.014.2297</div>
<div class="abs contact" style="left:402px;top:3937px">EMAIL US<br>hello@brightwaterdripclinic.com</div>
<div class="abs contact" style="left:818px;top:3915px">LOCATION<br>1420 Harbor Crest Blvd.<br>Lakeside, FL 30117</div>

</body>
</html>
```